T.K.R.A.C. Soccer Tryouts 2015-2016

I am looking for a soccer tryout flyer that stands out and catches peoples attention. An emphasis can be put on the cost, since we are by far the lowest cost program in the area. Below are the details for the flyer. I have also attached the club logo and pictures that can be used if needed.

T.K.R.A.C. SOCCER TRYOUTS
2015-2016

Club Fee: $699.00 per player

Tryout Schedule

Boys ages U9 through U14
Weds. May 27th and Friday May 29th
6:00 pm - 8:00 pm

Girls ages U9 through U14
Tuesday May 26th and Thursday May 28th
6:00 pm - 8:00 pm

All tryouts will be held at PLOV Fields
(Next to Gritmark Hardware factory at the corner of Rt. 342 and Hollow Brook Road)

We are encouraging all players to pre-register

Same Day Registrations will begin at 5:30

All players should bring a properly inflated ball, shin guards and water.

In the event of inclement weather, the tryouts will be moved to the JET indoor facility located at 4827 Dunmore Lane in Pine Hollow. The scheduled time slots will remain the same.

Website: www.tkracsoccer-example.com

Target Market(s)

Youth Soccer

Requirements
Must have
• Logo

```html
<!DOCTYPE html>
<html lang="en">
<head>
<meta charset="utf-8">
<title>T.K.R.A.C. Soccer Tryouts 2015-2016</title>
<link rel="stylesheet" href="https://fonts.googleapis.com/css2?family=Oswald:wght@600;700&family=Arimo:wght@400;700&display=swap">
<style>
  :root {
    --royal: #2f2fc9;
    --grass: #2f9a1e;
    --grass-dark: #1f6e14;
    --ink-green: #1d4a1d;
    --fee-yellow: #f4e60a;
    --white: #ffffff;
    --bg-light: #f4f5f4;
    --bg-mid: #d8dbd8;
    --rule: #9fbf98;
    --photo-a: #7f9a5c;
    --photo-b: #8fa6b8;
    --photo-c: #5d6f52;
    --photo-d: #a9b7c4;
  }
  * { margin: 0; padding: 0; box-sizing: border-box; }
  html, body { width: 848px; height: 1200px; overflow: hidden; }
  body { background: var(--bg-mid); font-family: "Arimo", Arial, sans-serif; }
  .flyer {
    position: relative; width: 848px; height: 1200px; overflow: hidden;
    background: radial-gradient(ellipse at 50% 45%, var(--white) 0%, var(--bg-light) 40%, var(--bg-mid) 100%);
  }
  .club-mark { position: absolute; left: 40px; top: 30px; width: 260px; text-align: center; z-index: 2; }
  .club-mark__dot { width: 150px; height: 150px; border-radius: 50%; background: var(--royal); margin: 0 auto 14px; }
  .club-mark__name { font-family: "Oswald", Impact, sans-serif; font-weight: 700; font-size: 40px; color: var(--royal); letter-spacing: 1px; }
  .headline { position: absolute; left: 330px; width: 500px; top: 38px; text-align: center; font-family: "Oswald", Impact, sans-serif; font-weight: 700; }
  .headline__club { font-size: 84px; line-height: 1; color: var(--royal); letter-spacing: 1px; }
  .headline__title { font-size: 54px; line-height: 1.1; color: var(--royal); margin-top: 4px; }
  .headline__season { font-size: 40px; line-height: 1.2; color: var(--ink-green); font-weight: 600; }
  .fee-band { position: absolute; left: 0; top: 268px; width: 848px; height: 48px; background: var(--grass);
    display: flex; align-items: center; justify-content: flex-end; padding-right: 34px; color: var(--white);
    font-weight: 700; font-size: 25px; }
  .fee-band__amount { color: var(--fee-yellow); font-size: 38px; margin: 0 8px; font-family: "Oswald", Impact, sans-serif; }
  .gallery { position: absolute; left: 20px; top: 339px; width: 810px; height: 340px; border-radius: 12px;
    background: var(--grass); border: 4px solid var(--grass-dark); }
  .gallery__photo { position: absolute; border-radius: 8px; border: 2px solid var(--white); }
  .schedule-heading { position: absolute; top: 700px; left: 0; width: 848px; text-align: center; font-family: "Oswald", Impact, sans-serif;
    font-weight: 700; font-size: 30px; color: var(--royal); text-decoration: underline; letter-spacing: 1px; }
  .schedule { position: absolute; top: 748px; left: 0; width: 848px; display: flex; }
  .schedule__group { width: 50%; text-align: center; color: var(--ink-green); font-size: 17.5px; line-height: 1.35; }
  .schedule__divider { position: absolute; left: 424px; top: 0; height: 70px; border-left: 2px dotted var(--grass); }
  .details { position: absolute; top: 848px; left: 40px; width: 768px; text-align: center; color: var(--ink-green); font-size: 20px; line-height: 1.4; }
  .details__item { padding: 4px 0 6px; border-bottom: 2px dotted var(--rule); }
  .details__item:last-child { border-bottom: none; }
  .site-band { position: absolute; left: 0; top: 1140px; width: 848px; height: 40px; background: var(--grass);
    display: flex; align-items: center; justify-content: center; color: var(--fee-yellow); font-weight: 700; font-size: 22px; }
</style>
</head>
<body>
<div class="flyer">
  <div class="club-mark">
    <div class="club-mark__dot"></div>
    <div class="club-mark__name">T.K.R.A.C.</div>
  </div>

  <div class="headline">
    <div class="headline__club">T.K.R.A.C.</div>
    <div class="headline__title">SOCCER TRYOUTS</div>
    <div class="headline__season">2015-2016</div>
  </div>

  <div class="fee-band">Club Fee: <span class="fee-band__amount">$699.00</span> per player</div>

  <div class="gallery">
    <div class="gallery__photo" role="img" aria-label="Boy player kicking the ball on grass" style="left:7px;top:6px;width:148px;height:318px;background:linear-gradient(var(--photo-c),var(--photo-a));"></div>
    <div class="gallery__photo" role="img" aria-label="Young players celebrating on the field" style="left:166px;top:6px;width:150px;height:98px;background:var(--photo-a);"></div>
    <div class="gallery__photo" role="img" aria-label="Girls team group photo" style="left:326px;top:6px;width:150px;height:98px;background:var(--photo-c);"></div>
    <div class="gallery__photo" role="img" aria-label="Girls team in light blue kits" style="left:486px;top:6px;width:150px;height:98px;background:var(--photo-b);"></div>
    <div class="gallery__photo" role="img" aria-label="Players running on the field" style="left:166px;top:116px;width:150px;height:96px;background:var(--photo-a);"></div>
    <div class="gallery__photo" role="img" aria-label="Team huddle after a match" style="left:326px;top:116px;width:150px;height:96px;background:var(--photo-c);"></div>
    <div class="gallery__photo" role="img" aria-label="Team lined up at a stadium" style="left:486px;top:116px;width:150px;height:96px;background:var(--photo-d);"></div>
    <div class="gallery__photo" role="img" aria-label="Girls team posing in blue kits" style="left:166px;top:224px;width:150px;height:100px;background:var(--photo-b);"></div>
    <div class="gallery__photo" role="img" aria-label="Team celebrating with arms raised" style="left:326px;top:224px;width:150px;height:100px;background:var(--photo-d);"></div>
    <div class="gallery__photo" role="img" aria-label="Team photo with coach" style="left:486px;top:224px;width:150px;height:100px;background:var(--photo-c);"></div>
    <div class="gallery__photo" role="img" aria-label="Girl player holding a ball on the field" style="left:648px;top:6px;width:148px;height:318px;background:linear-gradient(var(--photo-d),var(--photo-a));"></div>
  </div>

  <div class="schedule-heading">TRYOUT SCHEDULE</div>
  <div class="schedule">
    <div class="schedule__group">Boys ages U9 through U14<br>Wednesday May 27th and Friday May 29th<br>6:00 pm - 8:00 pm</div>
    <div class="schedule__divider"></div>
    <div class="schedule__group">Girls ages U9 through U14<br>Tuesday May 26th and Thursday May 28th<br>6:00 pm - 8:00 pm</div>
  </div>

  <div class="details">
    <div class="details__item">All tryouts will be held at PLOV Fields<br>(Next to Gritmark Hardware factory at the corner of Rt. 342 and Hollow Brook Road)</div>
    <div class="details__item">We are encouraging all players to pre-register</div>
    <div class="details__item">Same Day Registrations will begin at 5:30</div>
    <div class="details__item">All players should bring a properly inflated ball, shin guards and water.</div>
    <div class="details__item">In the event of inclement weather, the tryouts will be moved to the JET<br>indoor facility located at 4827 Dunmore Lane in Pine Hollow.<br>The scheduled time slots will remain the same.</div>
  </div>

  <div class="site-band">www.tkracsoccer-example.com</div>
</div>
</body>
</html>
```